Web design - holistic filmmaker

I need a design for my new website.

I am a holistic filmmaker, ie I make films for healers, alternative practitioners, spiritual people and institutions that offer training in this field.

The design should be noble, bright, convey the feeling of space and expanse and have some particularly beautiful color accents.

The structure is: start page, offer, references, about me, imprint.

As an idea for the start page, I thought that either I could introduce myself as a filmmaker and my offer, or we could start right on the start page with the references, ie photos and links to already realized projects.

If you want more information or an exchange, I'd love to hear from you. At the moment I just don't know how to describe it better.

The winner will then be asked to design a logo.

Target Market(s)

healers, alternative practitioners, spiritual people and institutions that offer training in this field

Industry/Entity Type

Film production

Number of Pages Required

3 page

```html
<!DOCTYPE html>
<html lang="en">
<head>
<meta charset="utf-8">
<title>Milo Film Maker – Holistic Filmmaker</title>
<link rel="stylesheet" href="https://fonts.googleapis.com/css2?family=Oswald:wght@300;400&family=Montserrat:wght@400;500;600&display=swap">
<style>
:root{
  --blue:#0d6fc4;
  --orange:#f7a21b;
  --ink:#1d1d1d;
  --text:#2b2b2b;
  --muted:#555;
  --white:#fff;
  --footer:#050505;
  --head:"Oswald",sans-serif;
  --body:"Montserrat",sans-serif;
}
*{margin:0;padding:0;box-sizing:border-box}
html,body{width:1200px;height:3419px;overflow:hidden;background:var(--white)}
body{position:relative;font-family:var(--body);color:var(--text)}
.abs{position:absolute}
a{text-decoration:none;color:inherit}

/* header */
.brand{display:flex;align-items:center;gap:12px}
.brand-mark{background:var(--orange)}
.brand-name{font-family:var(--head);font-weight:400;color:var(--blue);line-height:1}
.site-header .brand{left:98px;top:15px}
.site-header .brand-mark{width:48px;height:56px}
.site-header .brand-name{font-size:30px}
.nav{top:33px;left:678px;display:flex;gap:28px;font-size:15px;font-weight:500;color:var(--ink)}
.nav .active{color:var(--orange)}

/* hero */
.hero-photo{left:587px;top:89px;width:613px;height:569px;background:linear-gradient(135deg,#2d2b26 0%,#6a5a48 45%,#c77a1e 75%,#3a3834 100%)}
.hero-deco{left:98px;top:165px;width:340px;height:418px;background:#fff6ea}
.hero-title{left:101px;top:232px;width:470px;font-family:var(--head);font-weight:400;font-size:50px;line-height:64px;color:var(--blue)}
.hero-title span,.section-title span{color:var(--orange)}
.hero-sub{left:101px;top:368px;font-family:var(--head);font-weight:300;font-size:31px;line-height:52px;color:var(--ink)}
.text-link{font-size:18px;font-weight:500;color:var(--orange);border-bottom:1px solid var(--orange);padding-bottom:2px}
.hero-link{left:101px;top:476px}

/* sections */
.section-title{width:1200px;text-align:center;font-family:var(--head);font-weight:400;font-size:46px;color:var(--blue);line-height:1}
.refs-title{top:760px}
.refs-intro{top:812px;left:120px;width:960px;text-align:center;font-size:13.5px;line-height:27px;color:var(--ink)}
.ref-card{top:890px;width:491px}
.ref-media{height:268px;background:linear-gradient(120deg,#6d5b4e,#b79c86 40%,#8a3c56 75%,#4d4a3e);position:relative}
.ref-card:nth-of-type(2) .ref-media{background:linear-gradient(120deg,#3e4a2e,#8c8a78 40%,#c23a32 75%,#5c4b2c)}
.play{position:absolute;left:198px;top:100px;width:98px;height:70px;border-radius:16px;background:rgba(232,40,30,.8)}
.play::after{content:"";position:absolute;left:40px;top:22px;border-left:24px solid rgba(255,255,255,.7);border-top:13px solid transparent;border-bottom:13px solid transparent}
.ref-name{margin:20px 0 0 3px;font-family:var(--head);font-weight:300;font-size:26px;color:var(--ink)}
.ref-text{margin:10px 0 0 3px;font-size:13.5px;line-height:27px;color:var(--ink)}
.ref-card .text-link{display:inline-block;margin:10px 0 0 2px}
.slider-arrow{top:1000px;width:48px;height:48px;border-radius:50%;background:#fdf1dd}
.slider-arrow svg{width:48px;height:48px}

/* passion */
.passion-band{left:0;top:1412px;width:1200px;height:514px;background:linear-gradient(100deg,#a7742e 0%,#6e4f2e 35%,#4a3a32 60%,#2f2e34 100%)}
.passion-title{left:101px;top:1748px;font-family:var(--head);font-weight:400;font-size:44px;color:var(--white);line-height:1}
.passion-sub{left:101px;top:1798px;font-family:var(--head);font-weight:300;font-size:27px;line-height:36px;color:var(--white)}
.feature{top:1905px;width:485px;height:170px;background:var(--white);border-top:5px solid var(--orange);box-shadow:0 4px 14px rgba(0,0,0,.08);display:flex;align-items:center;padding:0 30px 10px 22px;gap:26px}
.feature svg{flex:none;width:62px;height:62px}
.feature p{font-size:13.5px;line-height:28px;color:var(--ink)}

/* journey */
.journey{left:0;top:2178px;width:1200px;height:531px;background:linear-gradient(180deg,#f9c866 0%,#e3dc9c 50%,#9ed7cf 100%)}
.journey-photo{left:0;top:2178px;width:600px;height:531px;background:linear-gradient(90deg,#2a2a2a 0%,#6b6b66 45%,rgba(200,190,150,0) 100%)}
.journey-title{left:602px;top:2276px;font-family:var(--head);font-weight:400;font-size:42px;line-height:58px;color:var(--ink)}
.journey-text{left:602px;top:2398px;width:490px;font-size:17px;line-height:34px;color:#2a2a2a}
.journey-text p+p{margin-top:10px}

/* clients */
.clients-title{top:2810px}
.client{top:2900px;width:160px;height:150px;display:flex;align-items:center;justify-content:center;gap:10px;font-family:var(--head);font-weight:400;font-size:30px;color:var(--ink)}
.client i{width:18px;height:18px;border-radius:50%;background:var(--orange);display:block}

/* footer */
.site-footer{left:0;top:3146px;width:1200px;height:229px;background:var(--footer)}
.footer-deco{left:398px;top:3146px;width:183px;height:229px;background:#2a1d06}
.site-footer-brand{left:98px;top:3215px}
.site-footer-brand .brand-mark{width:76px;height:90px}
.site-footer-brand .brand-name{font-size:58px}
.contact{top:3238px;display:flex;gap:12px;align-items:center;color:var(--white)}
.contact .ico{width:42px;height:42px;border:1.5px solid var(--orange);display:flex;align-items:center;justify-content:center}
.contact b{display:block;font-size:16px;font-weight:500}
.contact span{font-size:15px;font-weight:500}
.copyright{left:0;top:3375px;width:1200px;height:44px;background:var(--orange);text-align:center;line-height:44px;font-size:13.5px;color:#222}
.copyright strong{font-weight:600}
</style>
</head>
<body>

<header class="site-header">
  <a class="brand abs" href="#"><i class="brand-mark"></i><span class="brand-name">MILO Film Maker</span></a>
  <nav class="nav abs">
    <a class="active" href="#">Home</a><a href="#">Offer</a><a href="#">References</a><a href="#">About Me</a><a href="#">Imprint</a>
  </nav>
</header>

<section class="hero">
  <div class="hero-deco abs"></div>
  <div class="hero-photo abs" role="img" aria-label="Portrait of the filmmaker in an orange shirt and grey jacket"></div>
  <h1 class="hero-title abs">My Name is <span>M</span>ilo &amp; I Do Movies</h1>
  <p class="hero-sub abs">With Enthusiasm And Wholeheartedly.<br>I Am A Hosistic Filmmaker.</p>
  <a class="text-link hero-link abs" href="#">Read More About Me</a>
</section>

<section class="references">
  <h2 class="section-title refs-title abs"><span>M</span>Y REFERENCES</h2>
  <p class="refs-intro abs">Lorem ipsum dolor sit amet, consectetuer adipiscing elit, sed diam nonummy nibh euismod tincidunt uLorem ipsum dolor sit amet, consectetuer adipiscing elit, sed diam nonummy nibh euismod tincidunt ut laoreet dolore magna.</p>
  <div class="slider-arrow abs" style="left:36px"><svg viewBox="0 0 48 48"><path d="M28 15 L19 24 L28 33" fill="none" stroke="#f7a21b" stroke-width="2"/></svg></div>
  <article class="ref-card abs" style="left:94px">
    <div class="ref-media" role="img" aria-label="Video still of a speaker presenting beside a flip chart"><span class="play"></span></div>
    <h3 class="ref-name">Lumara</h3>
    <p class="ref-text">Lorem ipsum dolor sit amet, consectetuer adipiscing elit, sed diam nonummy nibh euismod tincidunt uLorem ipsum...</p>
    <a class="text-link" href="#">Watch Video</a>
  </article>
  <article class="ref-card abs" style="left:607px">
    <div class="ref-media" role="img" aria-label="Video still of a group in a healing session"><span class="play"></span></div>
    <h3 class="ref-name">Verdalis</h3>
    <p class="ref-text">Lorem ipsum dolor sit amet, consectetuer adipiscing elit, sed diam nonummy nibh euismod tincidunt uLorem ipsum...</p>
    <a class="text-link" href="#">Watch Video</a>
  </article>
  <div class="slider-arrow abs" style="left:1104px"><svg viewBox="0 0 48 48"><path d="M20 15 L29 24 L20 33" fill="none" stroke="#f7a21b" stroke-width="2"/></svg></div>
</section>

<section class="passion">
  <div class="passion-band abs" role="img" aria-label="The filmmaker smiling with a camera on his shoulder among photographers"></div>
  <h2 class="passion-title abs">MY PASSION</h2>
  <p class="passion-sub abs">My Cinematic Path Took Me Literally From Cable Man To<br>Cameraman, Director And Producers</p>
  <div class="feature abs" style="left:98px">
    <svg viewBox="0 0 62 62" fill="none" stroke="#0d6fc4" stroke-width="2"><rect x="6" y="24" width="50" height="30" rx="3"/><path d="M6 24 L8 12 L54 8 L56 20 Z"/><path d="M16 11 L20 22 M28 10 L32 21 M40 9 L44 20"/><circle cx="31" cy="40" r="6" stroke="#f7a21b"/><path d="M29 37 L34 40 L29 43 Z" stroke="#f7a21b"/><path d="M10 40 H22 M40 40 H52"/></svg>
    <p>Lorem ipsum dolor sit amet, consectetuer adipiscing elit, sed diam nonummy nibh euismod tincidunt ut laoreet dolore magna aliquam.</p>
  </div>
  <div class="feature abs" style="left:618px">
    <svg viewBox="0 0 62 62" fill="none" stroke="#0d6fc4" stroke-width="2"><path d="M14 8 V30 M48 8 V30"/><rect x="20" y="6" width="22" height="14" stroke="#f7a21b"/><path d="M8 30 H54 M12 36 H50"/><path d="M16 36 L44 58 M46 36 L18 58"/></svg>
    <p>Erat volutpat ut wisi enim ad minim veniam, quis nostrud exerci tation ullamcorper suscipit lobortis nisl ut aliquip ex ea commodo.</p>
  </div>
</section>

<section>
  <div class="journey abs"></div>
  <div class="journey-photo abs" role="img" aria-label="Black and white portrait of the filmmaker laughing"></div>
  <h2 class="journey-title abs">Making A Movie is Always A<br>Journey To Yourself</h2>
  <div class="journey-text abs">
    <p>Films for Clarity is aimed at all people and institutions whose striving for truthfulness is the driving force behind their action.</p>
    <p>I accompany you on the way to portraying your essence, with simple means and withour special effects.</p>
  </div>
</section>

<section class="clients">
  <h2 class="section-title clients-title abs"><span>M</span>EINE KUNDEN</h2>
  <div class="client abs" style="left:133px">Lumara</div>
  <div class="client abs" style="left:401px"><i></i>Verdalis</div>
  <div class="client abs" style="left:655px"><i></i>Sunvale</div>
  <div class="client abs" style="left:878px;width:200px;font-size:26px">Eastbrook Stage</div>
</section>

<footer>
  <div class="site-footer abs"></div>
  <div class="footer-deco abs"></div>
  <a class="brand site-footer-brand abs" href="#"><i class="brand-mark"></i><span class="brand-name">MILO Film Maker</span></a>
  <div class="contact abs" style="left:710px">
    <span class="ico"><svg width="22" height="22" viewBox="0 0 22 22" fill="none" stroke="#fff" stroke-width="1.4"><rect x="2" y="5" width="18" height="13"/><path d="M2 5 L11 12 L20 5"/></svg></span>
    <div><b>Email</b><span>milo@example.com</span></div>
  </div>
  <div class="contact abs" style="left:925px">
    <span class="ico"><svg width="22" height="22" viewBox="0 0 22 22" fill="none" stroke="#fff" stroke-width="1.4"><path d="M5 3 L9 7 L7 10 C8 13 10 15 13 16 L15 14 L19 18 L16 20 C9 19 4 13 3 6 Z"/></svg></span>
    <div><b>Phone</b><span>555.014.2290</span></div>
  </div>
  <p class="copyright abs">© 2023. <strong>Milo Film Maker.</strong> All Rights Reserved.</p>
</footer>

</body>
</html>
```